Premier nutraceutical company needs a label design.

We need a label design for a new product we're launching called Velvet Cinderoak. Our company name, Brivamos, will be at the top of the label. I'll upload relevant files of different looks that I like.

```html
<!DOCTYPE html>
<html lang="en">
<head>
<meta charset="utf-8">
<title>Brivamos – Velvet Phyto Cinderoak Label</title>
<link href="https://fonts.googleapis.com/css2?family=Josefin+Sans:wght@600&family=Montserrat:wght@500;800&family=Open+Sans:wght@400;600&family=Damion&display=swap" rel="stylesheet">
<style>
  :root {
    --backdrop: #f4f5f5;
    --label-white: #ffffff;
    --ink: #2c3133;
    --ink-soft: #3d4346;
    --teal: #3ea8a8;
    --teal-light: #7cc9c7;
    --teal-deep: #26807f;
    --script-teal: #1f5d5e;
    --pill: #1f4b4c;
    --pill-text: #ffffff;
  }
  * { margin: 0; padding: 0; box-sizing: border-box; }
  html, body {
    width: 1200px;
    height: 1200px;
    overflow: hidden;
    background: var(--backdrop);
  }
  .canvas {
    position: relative;
    width: 1200px;
    height: 1200px;
  }
  .label {
    position: absolute;
    left: 150px;
    top: 210px;
    width: 900px;
    height: 780px;
    background: var(--label-white);
    border-radius: 6px;
    box-shadow: 0 2px 18px rgba(0, 0, 0, 0.06);
    overflow: hidden;
  }
  .label__band {
    position: absolute;
    left: 0;
    top: 0;
    width: 900px;
    height: 780px;
  }
  .brand-name {
    position: absolute;
    top: 70px;
    width: 100%;
    text-align: center;
    font-family: "Josefin Sans", sans-serif;
    font-weight: 600;
    font-size: 86px;
    letter-spacing: 7px;
    color: var(--ink);
  }
  .product-line {
    position: absolute;
    top: 250px;
    width: 100%;
    text-align: center;
    font-family: "Montserrat", sans-serif;
    font-weight: 500;
    font-size: 66px;
    letter-spacing: 2px;
    color: var(--ink-soft);
  }
  .product-title {
    position: absolute;
    top: 318px;
    width: 100%;
    text-align: center;
    font-family: "Montserrat", sans-serif;
    font-weight: 800;
    font-size: 106px;
    letter-spacing: 3px;
    color: var(--ink);
  }
  .product-script {
    position: absolute;
    top: 452px;
    width: 100%;
    text-align: center;
    font-family: "Damion", cursive;
    font-size: 78px;
    color: var(--script-teal);
    transform: rotate(-3deg);
  }
  .capsule-count {
    position: absolute;
    top: 596px;
    left: 50%;
    transform: translateX(-50%);
    padding: 8px 34px;
    background: var(--pill);
    border-radius: 30px;
    font-family: "Open Sans", sans-serif;
    font-weight: 600;
    font-size: 28px;
    letter-spacing: 1px;
    color: var(--pill-text);
    white-space: nowrap;
  }
  .supplement-note {
    position: absolute;
    top: 666px;
    width: 100%;
    text-align: center;
    font-family: "Open Sans", sans-serif;
    font-weight: 400;
    font-size: 34px;
    color: var(--ink);
  }
</style>
</head>
<body>
  <main class="canvas">
    <section class="label">
      <svg class="label__band" viewBox="0 0 900 780" aria-hidden="true">
        <defs>
          <linearGradient id="bandFill" x1="0" y1="0" x2="1" y2="1">
            <stop offset="0" stop-color="#3aa3a3"/>
            <stop offset="0.55" stop-color="#46b0ae"/>
            <stop offset="1" stop-color="#2f9695"/>
          </linearGradient>
        </defs>
        <path d="M0 430 C 220 500, 520 360, 900 420 L 900 735 C 620 770, 300 700, 0 745 Z" fill="url(#bandFill)"/>
        <path d="M0 470 C 260 520, 560 420, 900 470" fill="none" stroke="var(--teal-light)" stroke-width="6" opacity="0.55"/>
        <path d="M0 540 C 300 590, 600 500, 900 560" fill="none" stroke="var(--teal-light)" stroke-width="3" opacity="0.4"/>
      </svg>
      <div class="brand-name">Brivamos</div>
      <div class="product-line">VELVET</div>
      <div class="product-title">PHYTO</div>
      <div class="product-script">cinderoak</div>
      <div class="capsule-count">60 VEGETABLE CAPSULES</div>
      <div class="supplement-note">Dietary Supplement</div>
    </section>
  </main>
</body>
</html>
```